Architecture firm needing a business card

We need a business card design for a new company based in the US called "Pellmore Architecture". Seeking minimalist designs that have a creativity/design feel but must be clean and professional. Please refer to the logo attached.

Target Market(s)

Real Estate Investors, Home Builders and Construction Firms.

Industry/Entity Type

Architecture

Contact Information for Business Card

Standard US size business cards. Would like to have some sort of graphic on the back side of the card - nothing that is too loud but something that may catch your attention. More or less grayscale colors that are in line with the logo colors (navy and greys essentially). Additional colors maybe accepted if blended properly (earthtones), but might be difficult to accomplish and maintain the clean/minimalist look.

Requirements
Must have
• Clean Lines
Nice to have
• some sort of graphics, would like to have something creative on the back side of the card
Should not have
• nothing too busy, cluttered or overwhelming.

```html
<!DOCTYPE html>
<html lang="en">
<head>
<meta charset="utf-8">
<title>Pellmore Architecture – Business Card</title>
<link rel="stylesheet" href="https://fonts.googleapis.com/css2?family=Cabin:wght@400;600;700&display=swap">
<style>
  :root {
    --navy: #123f6b;
    --grey: #9a9a98;
    --grey-text: #8a8a8a;
    --ink: #1c1c1e;
    --icon-blue: #2f86cf;
    --paper: #ffffff;
    --backdrop: #34434e;
  }
  * { box-sizing: border-box; margin: 0; padding: 0; }
  html, body { width: 1200px; height: 1200px; overflow: hidden; }
  body {
    background: var(--backdrop);
    font-family: "Cabin", sans-serif;
    display: flex;
    flex-direction: column;
    align-items: center;
    justify-content: center;
    gap: 64px;
  }
  .card {
    position: relative;
    width: 880px;
    height: 503px;
    overflow: hidden;
    box-shadow: 0 18px 40px rgba(0,0,0,.35);
  }

  /* Back side */
  .card-back { background: var(--navy); }
  .back-band {
    position: absolute; left: 0; right: 0; top: 108px; height: 196px;
    background: var(--paper);
  }
  .back-block {
    position: absolute; top: 124px; height: 164px; width: 132px;
    background: var(--grey);
  }
  .back-block.left { left: 0; }
  .back-block.right { right: 0; }
  .back-brand {
    position: absolute; left: 160px; right: 160px; top: 108px; height: 196px;
    display: flex; align-items: center; justify-content: center; gap: 26px;
    color: var(--navy);
    font-weight: 600;
  }
  .brand-square { width: 58px; height: 58px; background: var(--navy); flex: none; }
  .brand-name { line-height: 1; }
  .back-brand .brand-word { display: block; font-size: 70px; letter-spacing: 2px; }
  .back-brand .brand-sub { display: block; font-size: 28px; letter-spacing: 12px; margin-top: 8px; }

  /* Front side */
  .card-front { background: var(--paper); }
  .front-brand {
    position: absolute; left: 40px; top: 84px; width: 340px;
    display: flex; flex-direction: column; align-items: center;
    color: var(--navy); font-weight: 600; text-align: center;
  }
  .front-brand .brand-square { width: 92px; height: 92px; margin-bottom: 34px; }
  .front-brand .brand-word { display: block; font-size: 60px; letter-spacing: 1px; line-height: 1; }
  .front-brand .brand-sub { display: block; font-size: 25px; letter-spacing: 9px; margin-top: 10px; }
  .divider {
    position: absolute; left: 420px; top: 110px; height: 290px;
    border-left: 2px dotted #b9b9b9;
  }
  .contact { position: absolute; left: 478px; top: 66px; color: var(--ink); }
  .person-name { font-size: 31px; line-height: 37px; font-weight: 700; color: var(--navy); }
  .person-role { font-size: 21px; line-height: 25px; color: var(--grey-text); letter-spacing: 1px; margin-top: 2px; }
  .contact-list { list-style: none; margin-top: 22px; }
  .contact-list li {
    display: flex; align-items: center; gap: 16px;
    font-size: 28px; line-height: 38px;
  }
  .contact-list svg { width: 26px; height: 26px; flex: none; fill: var(--icon-blue); }
  .address { margin-top: 22px; font-size: 28px; line-height: 38px; font-style: normal; }
  .front-footer { position: absolute; left: 0; bottom: 0; width: 880px; height: 62px; }
</style>
</head>
<body>

<section class="card card-back" aria-label="Card back">
  <div class="back-band"></div>
  <div class="back-block left"></div>
  <div class="back-block right"></div>
  <div class="back-brand">
    <span class="brand-square"></span>
    <span class="brand-name">
      <span class="brand-word">PELLMORE</span>
      <span class="brand-sub">ARCHITECTURE</span>
    </span>
  </div>
</section>

<section class="card card-front" aria-label="Card front">
  <div class="front-brand">
    <span class="brand-square"></span>
    <span class="brand-word">PELLMORE</span>
    <span class="brand-sub">ARCHITECTURE</span>
  </div>

  <div class="divider"></div>

  <div class="contact">
    <p class="person-name">Name Here</p>
    <p class="person-role">Position</p>
    <ul class="contact-list">
      <li>
        <svg viewBox="0 0 24 24" aria-label="Mobile"><path d="M7 1h10a2 2 0 0 1 2 2v18a2 2 0 0 1-2 2H7a2 2 0 0 1-2-2V3a2 2 0 0 1 2-2zm0 3v15h10V4z"/></svg>
        (807) 123-4567
      </li>
      <li>
        <svg viewBox="0 0 24 24" aria-label="Phone"><path d="M2 8c0-3 4-5 10-5s10 2 10 5v2h-5V8H7v2H2zM6 12h12l2 9H4zm6 2a3 3 0 1 0 0 6 3 3 0 0 0 0-6z"/></svg>
        (807) 123-4567
      </li>
      <li>
        <svg viewBox="0 0 24 24" aria-label="Fax"><path d="M3 7h4v15H3zM9 2h9l3 3v17H9zm2 10v2h2v-2zm4 0v2h2v-2zm-4 4v2h2v-2zm4 0v2h2v-2zM11 5v4h8V5z"/></svg>
        (807) 123-4567
      </li>
      <li>
        <svg viewBox="0 0 24 24" aria-label="Email"><path d="M1 5h22v14H1zm2 2v10l6-5zm18 0-6 5 6 5zM4 6l8 7 8-7z"/></svg>
        name@email.com
      </li>
    </ul>
    <address class="address">Address Street<br>City State Zip</address>
  </div>

  <svg class="front-footer" viewBox="0 0 880 62" aria-hidden="true">
    <rect x="0" y="34" width="600" height="28" fill="#1c1c1e"/>
    <polygon points="620,0 880,0 880,62 604,62" fill="#123f6b"/>
    <polygon points="705,0 719,0 703,62 689,62" fill="#ffffff"/>
  </svg>
</section>

</body>
</html>
```